Church needs an introductory/informative postcard

We are looking for a postcard that would introduce our church along with having our programing information. We need it to be in Spanish, I can provide the necessary translation. Please provide us with ideas for a tag line that invites people to come check us out. We can provide a bible scripture if necessary, but would like something short that projects interest and confidence. We have a logo that we would like incorporated.

Target Market(s)

Hispanic

Industry/Entity Type

Religious

Requirements
Must have
• Colorful to coordinate with our logo so it flows well
• Have an tag line that invites people to our church
Nice to have
• have a modern feel
• if needed we can provide some pictures of our building
Should not have
• Pictures of people

```html
<!DOCTYPE html>
<html lang="es">
<head>
<meta charset="utf-8">
<title>Comunidad Cristiana Betania – Postal</title>
<link rel="stylesheet" href="https://fonts.googleapis.com/css2?family=Cinzel:wght@400;600&family=Oswald:wght@500;600&family=Roboto+Condensed:wght@700&family=Lato:wght@400;700&display=swap">
<style>
  :root {
    --stage: #8c8c8c;
    --orange: #ee5a24;
    --green: #7cc242;
    --blue: #27a8e0;
    --ink: #111111;
    --paper: #ffffff;
    --stamp: #9a9a9a;
    --photo-top: #3e4a55;
    --photo-mid: #c9a77c;
    --photo-low: #7a4a2c;
  }
  * { margin: 0; padding: 0; box-sizing: border-box; }
  html, body { width: 907px; height: 1200px; overflow: hidden; }
  body { background: var(--stage); position: relative; }

  .postcard {
    position: absolute; left: 112px; width: 681px;
    background: var(--paper); overflow: hidden;
    box-shadow: 0 2px 6px rgba(0,0,0,.35);
  }
  .postcard svg.art { position: absolute; inset: 0; }

  /* front */
  .postcard--front { top: 37px; height: 525px; }
  .front__name {
    position: absolute; left: 46px; top: 358px;
    font-family: "Oswald", sans-serif; font-weight: 600; font-size: 28px;
    color: var(--ink); letter-spacing: 1px; line-height: 1.2;
  }
  .front__tagline { position: absolute; right: 22px; top: 338px; text-align: right; }
  .tagline__lead {
    font-family: "Cinzel", serif; font-weight: 400; font-size: 27px;
    color: var(--orange); line-height: 1;
  }
  .tagline__main {
    font-family: "Oswald", sans-serif; font-weight: 600; font-size: 21px;
    color: var(--ink); line-height: 1.35; letter-spacing: .2px;
  }
  .front__web {
    position: absolute; left: 0; right: 0; top: 471px; height: 54px;
    display: flex; align-items: center; justify-content: center;
    font-family: "Oswald", sans-serif; font-weight: 500; font-size: 16px;
    letter-spacing: 4.6px; color: var(--paper);
  }

  /* back */
  .postcard--back { top: 632px; height: 528px; }
  .back__name {
    position: absolute; left: 46px; width: 180px; top: 70px; text-align: center;
    font-family: "Oswald", sans-serif; font-weight: 600; font-size: 19px;
    letter-spacing: 1px; color: var(--paper);
  }
  .services { position: absolute; left: 46px; width: 180px; top: 110px; text-align: center; }
  .services__title {
    display: block; background: var(--ink); color: var(--paper);
    border-radius: 13px; height: 26px; line-height: 26px;
    font-family: "Cinzel", serif; font-weight: 600; font-size: 19px; letter-spacing: 1px;
  }
  .services__list { list-style: none; margin-top: 6px; }
  .services__list li {
    font-family: "Roboto Condensed", sans-serif; font-weight: 700; font-size: 15px;
    color: var(--paper); height: 34px; line-height: 34px;
  }
  .contact {
    position: absolute; left: 16px; top: 287px;
    font-family: "Lato", sans-serif; font-size: 13.5px; color: var(--paper); line-height: 1.3;
  }
  .contact__org { color: var(--orange); font-weight: 700; font-size: 12.5px; margin-bottom: 5px; }
  .contact__line { display: flex; align-items: flex-start; gap: 3px; }
  .contact__line svg { flex: none; margin-top: 3px; }
  .contact__indent { padding-left: 11px; }
  .contact__web { margin-top: 3px; font-size: 12.5px; }
  .stamp { position: absolute; left: 588px; top: 19px; width: 75px; height: 90px; background: var(--stamp); }
</style>
</head>
<body>

<section class="postcard postcard--front">
  <svg class="art" width="681" height="525" viewBox="0 0 681 525">
    <defs>
      <linearGradient id="photoTone" x1="0" y1="0" x2="0" y2="1">
        <stop offset="0" stop-color="var(--photo-top)"/>
        <stop offset=".35" stop-color="var(--photo-mid)"/>
        <stop offset="1" stop-color="var(--photo-low)"/>
      </linearGradient>
      <linearGradient id="crowdTone" x1="0" y1="0" x2="0" y2="1">
        <stop offset="0" stop-color="#ffffff"/>
        <stop offset="1" stop-color="#b7c9b9"/>
      </linearGradient>
    </defs>
    <rect width="681" height="380" fill="url(#photoTone)" role="img" aria-label="Foto: Biblia abierta sobre un muelle de madera junto a un lago con montañas al atardecer"/>
    <path d="M0,232 C110,176 250,196 340,370 C430,196 570,176 681,232 V471 H0 Z" fill="var(--paper)" transform="translate(0,26)"/>
    <rect x="0" y="400" width="681" height="57" fill="url(#crowdTone)" opacity=".8" role="img" aria-label="Silueta tenue de una congregación con manos alzadas"/>
    <path d="M0,232 C110,176 250,196 340,370 C430,196 570,176 681,232" fill="none" stroke="var(--orange)" stroke-width="16"/>
    <path d="M0,232 C110,176 250,196 340,370 C430,196 570,176 681,232" fill="none" stroke="var(--paper)" stroke-width="4" transform="translate(0,10)"/>
    <path d="M0,232 C110,176 250,196 340,370 C430,196 570,176 681,232" fill="none" stroke="var(--green)" stroke-width="6" transform="translate(0,15)"/>
    <path d="M0,232 C110,176 250,196 340,370 C430,196 570,176 681,232" fill="none" stroke="var(--paper)" stroke-width="4" transform="translate(0,20)"/>
    <path d="M0,232 C110,176 250,196 340,370 C430,196 570,176 681,232" fill="none" stroke="var(--blue)" stroke-width="6" transform="translate(0,25)"/>
    <rect x="0" y="457" width="681" height="4" fill="var(--blue)"/>
    <rect x="0" y="464" width="681" height="4" fill="var(--orange)"/>
    <rect x="0" y="471" width="681" height="54" fill="var(--ink)"/>
  </svg>
  <div class="front__name">BETANIA</div>
  <div class="front__tagline">
    <div class="tagline__lead">Vivimos para la</div>
    <div class="tagline__main">MISIÓN QUE CRISTO NOS DIO</div>
  </div>
  <div class="front__web">WWW.COMUNIDADBETANIA.ORG</div>
</section>

<section class="postcard postcard--back">
  <svg class="art" width="681" height="528" viewBox="0 0 681 528">
    <path d="M0,0 H300 C322,90 334,190 348,268 C312,330 262,390 222,436 H0 Z" fill="var(--orange)"/>
    <path d="M0,265 H346 C312,330 262,390 222,436 H0 Z" fill="var(--ink)"/>
    <rect x="0" y="254" width="346" height="4" fill="var(--green)"/>
    <rect x="0" y="259" width="350" height="4" fill="var(--blue)"/>
    <path d="M300,0 C322,90 334,190 348,268 C312,330 262,390 222,436" fill="none" stroke="var(--paper)" stroke-width="4" transform="translate(4,0)"/>
    <path d="M300,0 C322,90 334,190 348,268 C312,330 262,390 222,436" fill="none" stroke="var(--green)" stroke-width="5" transform="translate(10,0)"/>
    <path d="M300,0 C322,90 334,190 348,268 C312,330 262,390 222,436" fill="none" stroke="var(--blue)" stroke-width="5" transform="translate(21,0)"/>
  </svg>
  <div class="back__name">BETANIA</div>
  <div class="services">
    <span class="services__title">SERVICIOS</span>
    <ul class="services__list">
      <li>DOMINGO 11:00 AM</li>
      <li>MARTES 7:30 PM</li>
      <li>JUEVES 7:30 PM</li>
    </ul>
  </div>
  <div class="contact">
    <div class="contact__org">Comunidad Cristiana</div>
    <div class="contact__line">
      <svg width="8" height="11" viewBox="0 0 8 11"><path d="M4,0 A4,4 0 0 1 8,4 C8,7 4,11 4,11 C4,11 0,7 0,4 A4,4 0 0 1 4,0 Z" fill="var(--orange)"/><circle cx="4" cy="4" r="1.5" fill="var(--ink)"/></svg>
      <span>Betania</span>
    </div>
    <div class="contact__indent">2417 Alder St.</div>
    <div class="contact__indent">Cedar Vale, TX 75123</div>
    <div class="contact__line contact__web">
      <svg width="8" height="8" viewBox="0 0 8 8"><circle cx="4" cy="4" r="4" fill="var(--orange)"/></svg>
      <span>www.comunidadbetania.org</span>
    </div>
  </div>
  <div class="stamp"></div>
</section>

</body>
</html>
```